Fern Vale Ridgecrest Music Festival Poster

We are a summer music festival with concerts spanning Jazz, Cabaret, Education, Broadway, Chamber and Opera. We are looking for our key art for the 2016 season. This design will serve as the basis for all promotional materials, the concert program, and our web materials. Though eventually this means we will need to adjust the design to fit many different sizes, our poster will be printed mostly on 8.5" x 11" paper, and we can adapt from there. The design will be featured online and in print. It should be vertical and not landscape.

WE ARE SEEKING SLEEK, ELEGANT DESIGNS WITH MAYBE A KEY STOCK PHOTOGRAPH AND THE RELEVANT TEXT/DETAILS.

PLEASE NOTE: The included file "avenir logo.psd" is just a suggestion for the feel we are going for. It is our "working logo" after having scraped our old logo. We are interested in seeing your own ideas on how to style the brand name, but if you have ideas working with this version of the logo, feel free to use it.

REQUIRED DETAILS:
Festival Name: Fern Vale Ridgecrest Music Festival
Dates: July 29 - August 7 2016 (the year, 2016, must be included on the poster, but it does not need to be in the same location as where the actual dates are listed)
Website: www.fernvaleridgecrestfest.org

Additional Information:
- the 7 musical styles (jazz, choral, cabaret, education, broadway, chamber, opera) are important to defining who we are. You may decide to include these on the poster.
- We are looking for a very elegant design

TARGET:
We depend highly on an older clientele. We are working to expand our brand into younger demographics, but we want to be sure that we do not alienate our current consumer base with text that may be difficult for them to read.

Project Deadline Extended Reason: I am extending the deadline because it is taking longer to get feedback from my superiors than I had expected. Extending the deadline will give me time to provide adequate feedback from the people who will ultimately be making the decision. Thank you. Added Saturday, January 30, 2016

Sorry for the delay. There were issues with the decision makers but we are selecting in the next 24 hours.

Target Market(s)

Lovers of the styles of music we feature. We have a good number of elderly consumers, but also families and school groups (discussed further in description section)

Industry/Entity Type

Entertainment

Font styles to use
Sans Serif

Requirements
Must have
• Festival Name: Fern Vale Ridgecrest Music Festival
• Dates: July 29 - August 7 2016 (the year, 2016, must be included on the poster, but it does not need to be in the same location as where the actual dates are listed)
• Website: www.fernvaleridgecrestfest.org
Nice to have
• - the 7 musical styles (jazz, choral, cabaret, education, broadway, chamber, opera) are important to defining who we are. We would love to include these styles somewhere on the image, or feature them somehow in the artwork
• - Our brand has an elegance to it due to the type of music we offer, and our location being in a very natural space. inclusion of the music/nature mixed aspect of our brand in artwork might be nice
Should not have
• Anything that may offend or alienate an older, more conservative demographic

```html
<!DOCTYPE html>
<html lang="en">
<head>
<meta charset="utf-8">
<title>Fern Vale Ridgecrest Music Festival 2016</title>
<link href="https://fonts.googleapis.com/css2?family=Josefin+Sans:wght@400;600&display=swap" rel="stylesheet">
<style>
  :root {
    --page-bg: #f1f1f1;
    --paper: #ffffff;
    --title-white: #ffffff;
    --genre-plum: #4a2a33;
    --url-cream: #efdcd2;
    --art-top-a: #d08a70;
    --art-top-b: #a8605a;
    --art-top-c: #7d5468;
    --art-top-d: #b8553e;
    --art-low-a: #8a3a26;
    --art-low-b: #5e2320;
    --art-low-c: #3a1517;
  }
  * { margin: 0; padding: 0; box-sizing: border-box; }
  html, body {
    width: 1200px; height: 1107px; overflow: hidden;
    background: var(--page-bg);
    font-family: "Josefin Sans", sans-serif;
  }
  .poster {
    position: absolute; left: 219px; top: 40px;
    width: 762px; height: 1027px;
    background: var(--paper);
    overflow: hidden;
  }
  .art-upper {
    position: absolute; left: 0; top: 0; width: 762px; height: 410px;
    background:
      radial-gradient(ellipse at 30% 60%, rgba(125,84,104,.55), transparent 60%),
      radial-gradient(ellipse at 80% 30%, rgba(220,110,110,.5), transparent 55%),
      linear-gradient(160deg, var(--art-top-a) 0%, var(--art-top-b) 45%, var(--art-top-c) 75%, var(--art-top-d) 100%);
  }
  .art-lower {
    position: absolute; left: 0; top: 712px; width: 762px; height: 315px;
    background:
      radial-gradient(ellipse at 20% 40%, rgba(40,15,18,.6), transparent 55%),
      linear-gradient(170deg, var(--art-low-a) 0%, var(--art-low-b) 55%, var(--art-low-c) 100%);
  }
  .festival-name { font-weight: inherit; }
  .title {
    position: absolute; line-height: 1; white-space: nowrap;
    color: var(--title-white);
    text-shadow: 2px 2px 3px rgba(0,0,0,.35);
  }
  .title-music { left: 103px; top: 90px; font-size: 72px; font-weight: 600; }
  .title-place { left: 336px; top: 108px; font-size: 23px; font-weight: 400; }
  .title-festival { left: 100px; top: 152px; font-size: 102px; font-weight: 600; }
  .title-year { left: 586px; top: 160px; font-size: 26px; font-weight: 600; }
  .dates {
    position: absolute; left: 105px; top: 268px;
    color: var(--title-white); font-size: 24px; font-weight: 400;
    letter-spacing: 1px; line-height: 1;
    text-shadow: 1px 1px 3px rgba(0,0,0,.4);
  }
  .genres {
    position: absolute; left: 0; top: 472px; width: 762px;
    text-align: center; color: var(--genre-plum);
    font-size: 58px; font-weight: 600; line-height: 68px;
  }
  .url {
    position: absolute; left: 0; top: 950px; width: 762px;
    text-align: center; color: var(--url-cream);
    font-size: 22px; letter-spacing: 6px;
  }
</style>
</head>
<body>
  <main class="poster">
    <div class="art-upper" role="img" aria-label="Low-poly illustration of musicians performing in warm reds, pinks and purples, edged by a line of pine trees"></div>
    <h1 class="festival-name">
      <span class="title title-music">MUSIC</span>
      <span class="title title-place">FERN VALE RIDGECREST</span>
      <span class="title title-festival">FESTIVAL</span>
      <span class="title title-year">2016</span>
    </h1>
    <p class="dates">July 29 – August 7, 2016</p>
    <p class="genres">Jazz | Choral | Cabaret<br>Education | Broadway<br>Chamber | Opera</p>
    <div class="art-lower" role="img" aria-label="Low-poly illustration of a performer and instrument in deep reds and browns, topped by a line of pine trees"></div>
    <p class="url">www.fernvaleridgecrestfest.org</p>
  </main>
</body>
</html>
```